Design a poster that illustrates the six central pillars of our school district's efforts with students. The attached PDF outlines the six main competencies we aim for students to possess upon graduation. Each of the 6 has 3 bullet points for the poster as well. The title is "Profile of a Kestrel". Our mascot is this attached winged wheel. The overall concept is that staff take kids when they are young and develop these 6 things when they graduate. Our colors are navy, red, and white. We will make this poster in a variety of sizes in offices, classrooms, and in digital spaces as well. On the PDF - ignore the column that says "Synthesis". That has nothing to do with this poster.

The district is Harlow Creek Public Schools https://www.harlowcreek-schools.example/

```html
<!DOCTYPE html>
<html lang="en">
<head>
<meta charset="utf-8">
<title>Profile of a Kestrel — Harlow Creek Public Schools</title>
<link rel="stylesheet" href="https://fonts.googleapis.com/css2?family=Inter:wght@400;500;600;700&family=Montserrat:wght@800&family=Rubik:wght@700&display=swap">
<style>
  :root {
    --navy: #14114a;
    --navy-deep: #0f0d40;
    --red: #9e1b22;
    --ink: #1a1846;
    --rule: #6e6c8a;
    --rule-soft: #c9c8d6;
    --white: #ffffff;
    --paper-bg: #f4f4f7;
  }
  * { box-sizing: border-box; margin: 0; padding: 0; }
  html, body { width: 934px; height: 1200px; overflow: hidden; background: var(--paper-bg); }
  .poster {
    position: relative; width: 934px; height: 1200px; background: var(--white);
    font-family: "Inter", Arial, sans-serif; color: var(--ink); overflow: hidden;
  }

  /* Header */
  .masthead { position: absolute; left: 0; top: 0; width: 934px; height: 160px; }
  .masthead-mark {
    position: absolute; left: 176px; top: 46px; width: 80px; height: 80px;
    border-radius: 50%; border: 4px solid var(--navy); background: var(--white);
  }
  .masthead-name {
    position: absolute; left: 331px; top: 55px;
    font-weight: 700; font-size: 25px; color: var(--navy); letter-spacing: -0.2px;
  }
  .masthead-tagline {
    position: absolute; left: 331px; top: 85px;
    font-weight: 500; font-size: 22px; color: var(--ink); letter-spacing: -0.1px;
  }

  /* Title banner */
  .title-band {
    position: absolute; left: 0; top: 160px; width: 934px; height: 188px;
    background: linear-gradient(90deg, #15103f 0%, #5a1530 50%, #9e1b22 100%);
  }
  .title-band h1 {
    position: absolute; left: 0; right: 0; top: 26px; text-align: center;
    font-family: "Montserrat", Arial, sans-serif; font-weight: 800; font-size: 72px;
    line-height: 70px; color: var(--white); letter-spacing: -1px; text-transform: uppercase;
  }

  /* Pillars */
  .connectors { position: absolute; left: 0; top: 0; width: 934px; height: 1200px; }
  .pillar-label {
    position: absolute; height: 34px; display: flex; align-items: center; justify-content: center;
    background: linear-gradient(90deg, var(--navy-deep) 0%, #4a1535 55%, var(--red) 100%);
    font-family: "Rubik", Arial, sans-serif; font-weight: 700; font-size: 20px; color: var(--white);
  }
  .pillar-points {
    position: absolute; width: 226px; list-style: none; text-align: center;
    font-size: 13.4px; line-height: 17px; color: var(--ink);
  }
  .pillar-points li { position: relative; padding: 6px 0; }
  .pillar-points li:first-child { padding-top: 0; }
  .pillar-points li + li::before {
    content: ""; position: absolute; left: 23px; right: 23px; top: 0;
    border-top: 1px solid var(--rule-soft);
  }

  .district-seal {
    position: absolute; left: 417px; top: 668px; width: 100px; height: 100px;
    border-radius: 50%; border: 4px solid var(--navy); background: var(--white);
    display: flex; align-items: center; justify-content: center; text-align: center;
    font-weight: 700; font-size: 13px; line-height: 15px; color: var(--navy);
  }

  /* Footer */
  .footer-stripe { position: absolute; left: 0; top: 1088px; width: 934px; height: 7px; background: var(--red); }
  .footer { position: absolute; left: 0; top: 1095px; width: 934px; height: 105px; background: var(--navy-deep); color: var(--white); }
  .footer-contact { position: absolute; left: 70px; top: 31px; font-size: 14px; line-height: 20px; }
  .footer-contact strong, .footer-address strong { font-weight: 700; }
  .footer-address { position: absolute; right: 71px; top: 28px; text-align: right; font-size: 14px; line-height: 20px; }
</style>
</head>
<body>
<main class="poster">

  <header class="masthead">
    <div class="masthead-mark"></div>
    <p class="masthead-name">Harlow Creek Public Schools</p>
    <p class="masthead-tagline">Excellence in Academics, Arts &amp; Athletics</p>
  </header>

  <section class="title-band">
    <h1>Profile of<br>a Kestrel</h1>
  </section>

  <svg class="connectors" viewBox="0 0 934 1200" fill="none" stroke="#6e6c8a" stroke-width="1.2" aria-hidden="true">
    <!-- Communicator -->
    <path d="M93 452 H64 Q51 452 51 465 V647 Q51 660 64 660 H274"/>
    <circle cx="274" cy="660" r="3.6" fill="#6e6c8a" stroke="none"/>
    <!-- Responsible -->
    <path d="M314 549 V391 Q314 378 327 378 H601 Q614 378 614 391 V547"/>
    <circle cx="314" cy="549" r="3.6" fill="#6e6c8a" stroke="none"/>
    <circle cx="614" cy="547" r="3.6" fill="#6e6c8a" stroke="none"/>
    <!-- Collaborator -->
    <path d="M834 454 H869 Q882 454 882 467 V649 Q882 662 869 662 H659"/>
    <circle cx="659" cy="662" r="3.6" fill="#6e6c8a" stroke="none"/>
    <!-- Critical Thinker -->
    <path d="M85 710 H64 Q51 710 51 723 V904 Q51 917 64 917 H314"/>
    <!-- Adaptable -->
    <path d="M314 851 V1040 Q314 1053 327 1053 H601 Q614 1053 614 1040 V852"/>
    <circle cx="314" cy="851" r="3.6" fill="#6e6c8a" stroke="none"/>
    <circle cx="614" cy="852" r="3.6" fill="#6e6c8a" stroke="none"/>
    <!-- Compassionate -->
    <path d="M845 711 H866 Q879 711 879 724 V906 Q879 919 866 919 H614"/>
  </svg>

  <h2 class="pillar-label" style="left:93px; top:435px; width:189px;">Communicator</h2>
  <ul class="pillar-points" style="left:71px; top:493px;">
    <li>Expresses ideas clearly and respectfully (written &amp; verbal).</li>
    <li>Listens actively and understands diverse perspectives.</li>
    <li>Adjusts communication to suit the audience and context.</li>
  </ul>

  <h2 class="pillar-label" style="left:378px; top:393px; width:173px;">Responsible</h2>
  <ul class="pillar-points" style="left:351px; top:457px; width:226px;">
    <li>Takes ownership of actions, choices, and commitments now and in future aspirations.</li>
    <li>Takes pride in managing time, resources, and self while striving to meet high expectations.</li>
    <li>Acts with integrity while advocating for themselves and others.</li>
  </ul>

  <h2 class="pillar-label" style="left:661px; top:435px; width:173px;">Collaborator</h2>
  <ul class="pillar-points" style="left:634px; top:490px;">
    <li>Demonstrates strong teamwork by contributing effectively and cooperatively toward shared goals.</li>
    <li>Listens actively and values diverse ideas and perspectives.</li>
    <li>Engages respectfully, knowing when to compromise, support, or take the lead.</li>
  </ul>

  <div class="district-seal">Harlow<br>Creek</div>

  <h2 class="pillar-label" style="left:85px; top:693px; width:197px;">Critical Thinker</h2>
  <ul class="pillar-points" style="left:71px; top:749px;">
    <li>Questions, analyzes, and evaluates information from multiple sources.</li>
    <li>Identifies and solves complex problems creatively.</li>
    <li>Uses evidence and diverse perspectives to form reasoned conclusions and make informed decisions.</li>
  </ul>

  <h2 class="pillar-label" style="left:649px; top:693px; width:197px;">Compassionate</h2>
  <ul class="pillar-points" style="left:634px; top:749px;">
    <li>Understands and acknowledges others’ feelings, perspectives, and experiences.</li>
    <li>Responds with kindness, patience, empathy, and support.</li>
    <li>Seeks to connect with others and contribute positively to their well-being and the community’s well-being.</li>
  </ul>

  <h2 class="pillar-label" style="left:375px; top:804px; width:174px;">Adaptable</h2>
  <ul class="pillar-points" style="left:349px; top:862px;">
    <li>Responds productively to new situations, challenges, and constructive feedback.</li>
    <li>Learns from new experiences and applies prior knowledge in an ever-changing world.</li>
    <li>Adjusts behavior and approach to engage effectively with diverse groups and environments.</li>
  </ul>

  <div class="footer-stripe"></div>
  <footer class="footer">
    <p class="footer-contact"><strong>Phone: 616-555-0190</strong><br>www.harlowcreek-schools.example</p>
    <p class="footer-address"><strong>Harlow Creek Public Schools</strong><br>48 Meadow Lane, Harlow Creek, MI 49000</p>
  </footer>

</main>
</body>
</html>
```